IT supplier clean wordpress website - payment guaranteed

Clean website design for a wordpress based website
Design only - PSD delivery with images

current website: www.quilmo.net
please use your imagination and try something out of the box...
We like https://trevanly.com.au as look and feel, but you don't have to copy it, you can be creative

We like the navigation header and the phone number, but do not need 'instant quote' so the 1300 phone number and the 'lock' icon for login can be on the same line

Site Map:
IT support
VoIP
Internet and Data
Cloud hosting
About
Contact

Our logo is attached, it can be used light or dark.
Our only color used is the warm grey Pantone 8003C hex #877A69

You will only need to design the homepage to win the competition, but the winning designer will be required to supply without extra charges:
1. Home page design
2. A second, standard page template design
3. An icon set in colors appropriate to the site that have icons to match the subjects in these pages:
https://trevanly.com.au/products/
https://trevanly.com.au/making-the-switch/
https://trevanly.com.au/why-trevanly/
We will create a single page version of the options on https://trevanly.com.au/solutions/
4.Any images used

Please avoid stock photos that are too common - e.g. smiling woman with headset, try to make the design stand out with simple images and well-designed layout.

Mid-size business clients

It Company

1 page

• Quil logo
• Use Quil color

```html
<!DOCTYPE html>
<html lang="en">
<head>
<meta charset="utf-8">
<title>Quil – IT Support Business</title>
<link rel="stylesheet" href="https://fonts.googleapis.com/css2?family=Roboto:wght@300;400;500;700&display=swap">
<style>
:root{
  --orange:#f58220;
  --warm-grey:#877a69;
  --ink:#333333;
  --muted:#6b6b6b;
  --light-bg:#f0efed;
  --line:#d9d6d2;
  --white:#ffffff;
}
*{box-sizing:border-box;margin:0;padding:0}
html,body{width:1200px;height:3448px;overflow:hidden}
body{font-family:'Roboto',Arial,sans-serif;color:var(--ink);background:var(--white);position:relative}
section,header,footer{position:absolute;left:0;width:1200px}

/* header */
.site-header{top:0;height:130px;border-bottom:1px solid var(--line)}
.brand{position:absolute;left:36px;top:22px;display:flex;align-items:center;gap:12px}
.brand-mark{width:70px;height:70px;background:var(--warm-grey)}
.brand-name{font-size:30px;font-weight:500;color:var(--warm-grey)}
.main-nav{position:absolute;left:255px;top:80px;display:flex;gap:30px;font-size:13px;font-weight:500;color:var(--ink)}
.main-nav span{padding-bottom:8px}
.main-nav .active{border-bottom:3px solid var(--orange)}
.search-icon{position:absolute;left:1140px;top:79px}
.header-actions{position:absolute;right:30px;top:18px;display:flex;gap:12px}
.btn{background:var(--orange);color:var(--white);font-size:14px;font-weight:500;display:inline-flex;align-items:center;gap:8px;padding:9px 18px}
.header-actions .btn{font-size:13px;padding:8px 16px}

/* hero */
.hero{top:130px;height:590px}
.hero-copy{position:absolute;left:70px;top:90px;width:520px}
.hero-title{font-size:46px;font-weight:500;color:var(--ink);line-height:1.1}
.hero-tagline{font-size:44px;font-weight:400;color:var(--orange);margin-top:4px}
.tick-list{list-style:none;margin-top:28px}
.tick-list li{display:flex;gap:12px;font-size:16px;color:var(--muted);line-height:1.5;margin-bottom:14px}
.tick-list svg{flex:none;margin-top:4px}
.hero .btn{font-size:18px;padding:16px 40px;margin-top:18px}
.hero-photo{position:absolute;left:625px;top:20px;width:540px;height:540px;background:linear-gradient(135deg,#d8dde2,#8d97a1 55%,#3d4650)}

/* platform */
.platform{top:730px;height:555px;background:var(--light-bg)}
.section-title{text-align:center;font-size:40px;font-weight:400;color:var(--ink)}
.platform .section-title{margin-top:60px}
.feature-row{position:absolute;top:190px;left:0;width:1200px;display:flex;justify-content:center;gap:80px}
.feature{width:300px;text-align:center}
.feature h3{font-size:15px;font-weight:500;color:var(--ink);margin-top:24px}
.feature p{font-size:14px;color:var(--muted);margin-top:26px;line-height:1.5}

/* benefits */
.benefits{top:1285px;height:680px}
.benefits .section-title{margin-top:60px}
.benefit{position:absolute;width:260px}
.benefit h3{font-size:22px;font-weight:500;color:var(--ink)}
.benefit p{font-size:13px;color:var(--muted);line-height:1.35;margin-top:4px;width:190px}
.benefit-diagram{position:absolute;left:0;top:0}

/* about */
.about{top:1965px;height:545px;background:var(--light-bg)}
.about .section-title{margin-top:58px}
.about-copy{position:absolute;left:90px;top:165px;width:460px;font-size:16px;color:var(--muted);line-height:1.45}
.about-copy .established{font-size:18px;color:var(--ink);margin-bottom:12px}
.about-copy .sub{font-size:18px;color:var(--ink);margin:26px 0 8px}
.about-copy .tick-list{margin-top:16px}
.about-copy .tick-list li{color:var(--ink);margin-bottom:18px}
.about-photo{position:absolute;left:610px;top:140px;width:560px;height:300px;background:linear-gradient(135deg,#e7ecf0,#9fb2c3 50%,#4c6377)}

/* partners */
.partners{top:2510px;height:410px}
.partners .section-title{margin-top:70px}
.partner-row{position:absolute;top:200px;left:0;width:1200px;display:flex;justify-content:space-around;padding:0 60px}
.partner-badge{width:150px;height:60px;background:#c9c5c0}

/* footer */
.site-footer{top:2920px;height:528px}
.footer-panel{position:absolute;left:32px;top:30px;width:748px;height:470px;background:var(--warm-grey);color:var(--white)}
.footer-cols{position:absolute;left:70px;top:85px;display:flex;gap:55px}
.footer-cols h4{font-size:18px;font-weight:400;margin-bottom:14px}
.footer-cols li{list-style:none;font-size:13px;line-height:1.55}
.newsletter{position:absolute;left:70px;top:330px}
.newsletter p{font-size:13px;margin-bottom:14px}
.newsletter-field{width:290px;height:38px;border:1px solid rgba(255,255,255,.7);font-size:12px;padding:11px 10px;position:relative;color:rgba(255,255,255,.8)}
.newsletter-field svg{position:absolute;right:10px;top:13px}
.footer-brand{position:absolute;left:840px;top:50px;display:flex;align-items:center;gap:12px}
.footer-contact{position:absolute;left:840px;top:170px;font-size:18px;color:var(--ink);line-height:1.4}
.footer-contact .gap{margin-top:16px}
.copyright{position:absolute;left:0;top:500px;width:1200px;height:28px;background:var(--orange);color:var(--white);font-size:12px;text-align:center;line-height:28px}
</style>
</head>
<body>

<header class="site-header">
  <div class="brand"><span class="brand-mark"></span><span class="brand-name">Quil</span></div>
  <nav class="main-nav">
    <span class="active">WHY QUIL</span><span>IT SUPPORT</span><span>VOICE &amp; DATA</span><span>CLOUD COMPUTING</span><span>VOIP</span><span>ABOUT</span><span>CONTACT US</span>
  </nav>
  <svg class="search-icon" width="16" height="16" viewBox="0 0 16 16"><circle cx="6.5" cy="6.5" r="5" fill="none" stroke="#333" stroke-width="2"/><line x1="10" y1="10" x2="15" y2="15" stroke="#333" stroke-width="2"/></svg>
  <div class="header-actions">
    <span class="btn"><svg width="12" height="12" viewBox="0 0 12 12"><path d="M2 1h3l1 3-2 1a7 7 0 0 0 3 3l1-2 3 1v3c-6 1-10-3-9-9z" fill="#fff"/></svg>+61 (2) 5550 1122</span>
    <span class="btn"><svg width="12" height="14" viewBox="0 0 12 14"><rect x="1" y="6" width="10" height="8" fill="#fff"/><path d="M3 6V4a3 3 0 0 1 6 0v2" fill="none" stroke="#fff" stroke-width="1.6"/></svg>LOGIN</span>
  </div>
</header>

<section class="hero">
  <div class="hero-copy">
    <h1 class="hero-title">IT SUPPORT BUSINESS</h1>
    <p class="hero-tagline">Better.Easier.Faster</p>
    <ul class="tick-list">
      <li><svg width="16" height="13" viewBox="0 0 16 13"><path d="M1 7l5 5L15 1" fill="none" stroke="#f58220" stroke-width="3"/></svg>Quil is Secure and fully featured for all enterprises.</li>
      <li><svg width="16" height="13" viewBox="0 0 16 13"><path d="M1 7l5 5L15 1" fill="none" stroke="#f58220" stroke-width="3"/></svg>24/7 IT Support &amp; Management for businesses with between 5 and 500 people</li>
    </ul>
    <span class="btn">GET STARTED NOW</span>
  </div>
  <div class="hero-photo" role="img" aria-label="Businessman in a suit working on a laptop in a server room"></div>
</section>

<section class="platform">
  <h2 class="section-title">Why Quil Cloud Platform?</h2>
  <div class="feature-row">
    <div class="feature">
      <svg width="90" height="80" viewBox="0 0 90 80" fill="none" stroke="#f58220" stroke-width="2"><path d="M45 8l30 17v30L45 72 15 55V25z"/><rect x="33" y="28" width="24" height="24"/><path d="M39 28v-8M51 28v-8M39 52v8M51 52v8M33 34h-8M33 46h-8M57 34h8M57 46h8"/></svg>
      <h3>Future-Proof Infrastructure</h3>
      <p>At vero eos et accusamus et iusto odio<br>is praesentium</p>
    </div>
    <div class="feature">
      <svg width="90" height="80" viewBox="0 0 90 80" fill="none" stroke="#f58220" stroke-width="2"><path d="M5 40c10-30 20-30 30 0s20 30 30 0 15-25 20-10"/><path d="M5 40c10 30 20 30 30 0s20-30 30 0 15 25 20 10" opacity=".6"/></svg>
      <h3>Seriously Powerful Data &amp; Analytics</h3>
      <p>At vero eos et accusamus et iusto odio<br>is praesentium</p>
    </div>
    <div class="feature">
      <svg width="90" height="80" viewBox="0 0 90 80" fill="none" stroke="#f58220" stroke-width="2"><path d="M30 14c-8 0-8 4-8 12s-6 14-10 14c4 0 10 6 10 14s0 12 8 12M60 14c8 0 8 4 8 12s6 14 10 14c-4 0-10 6-10 14s0 12-8 12M38 30h14M36 40h18M38 50h14"/></svg>
      <h3>Serverless, Just Code</h3>
      <p>At vero eos et accusamus et iusto odio<br>is praesentium</p>
    </div>
  </div>
</section>

<section class="benefits">
  <h2 class="section-title">Benifits Of Cloud VOIP</h2>
  <svg class="benefit-diagram" width="1200" height="680" viewBox="0 0 1200 680">
    <g fill="none" stroke="#8a8a8a" stroke-width="1">
      <polyline points="120,180 370,180 390,210"/>
      <polyline points="1080,180 830,180 810,210"/>
      <polyline points="120,495 370,495 390,465"/>
      <polyline points="1080,495 830,495 810,465"/>
    </g>
    <circle cx="525" cy="340" r="105" fill="none" stroke="#8f8f8f" stroke-width="42"/>
    <path d="M675 235a105 105 0 1 1 0 210a105 105 0 1 1 0-210" fill="none" stroke="#f58220" stroke-width="42"/>
    <path d="M603 268a105 105 0 0 1 0 144" fill="none" stroke="#8f8f8f" stroke-width="42"/>
    <circle cx="525" cy="340" r="52" fill="#6f6f6f"/>
    <path d="M505 352h40a12 12 0 0 0 0-24a18 18 0 0 0-34 4a10 10 0 0 0-6 20z" fill="#fff"/>
    <circle cx="675" cy="340" r="52" fill="#f58220"/>
    <g fill="#fff"><ellipse cx="675" cy="318" rx="24" ry="8"/><rect x="651" y="318" width="48" height="42"/><ellipse cx="675" cy="360" rx="24" ry="8"/></g>
    <g stroke="#f58220" stroke-width="2"><path d="M651 332a24 8 0 0 0 48 0M651 346a24 8 0 0 0 48 0" fill="none"/></g>
    <circle cx="390" cy="210" r="14" fill="#333"/>
    <circle cx="810" cy="210" r="14" fill="#f58220"/>
    <circle cx="390" cy="465" r="14" fill="#333"/>
    <circle cx="810" cy="465" r="14" fill="#333"/>
  </svg>
  <div class="benefit" style="left:120px;top:108px"><h3>EASE IT WORKLOAD</h3><p>At vero eos et accusamus et iusto odio dignissimos sentium</p></div>
  <div class="benefit" style="left:830px;top:108px"><h3>KEEP UP TECHNOLOGY</h3><p>At vero eos et accusamus et iusto odio dignissimos sentium</p></div>
  <div class="benefit" style="left:120px;top:505px"><h3>EXPAND AS NECESSARY</h3><p>At vero eos et accusamus et iusto odio dignissimos sentium</p></div>
  <div class="benefit" style="left:830px;top:505px"><h3>EMBRANCE FLEXIBLITY</h3><p>At vero eos et accusamus et iusto odio dignissimos sentium</p></div>
</section>

<section class="about">
  <h2 class="section-title">WHO WE ARE</h2>
  <div class="about-copy">
    <p class="established">ESTABLISHED IN 1989</p>
    <p>Servicing industry's IT needs with experience in extensive technologies and platforms with a focus on customer service.</p>
    <p class="sub">Range of Skilled Engineers</p>
    <p>A range of skill-sets and qualifications with</p>
    <ul class="tick-list">
      <li><svg width="16" height="13" viewBox="0 0 16 13"><path d="M1 7l5 5L15 1" fill="none" stroke="#f58220" stroke-width="3"/></svg>CSA</li>
      <li><svg width="16" height="13" viewBox="0 0 16 13"><path d="M1 7l5 5L15 1" fill="none" stroke="#f58220" stroke-width="3"/></svg>NSE, NSP</li>
      <li><svg width="16" height="13" viewBox="0 0 16 13"><path d="M1 7l5 5L15 1" fill="none" stroke="#f58220" stroke-width="3"/></svg>NXE, NXP, NXA</li>
    </ul>
  </div>
  <div class="about-photo" role="img" aria-label="Close-up of network cables plugged into a switch"></div>
</section>

<section class="partners">
  <h2 class="section-title">SOME OF OUR PARTNERS</h2>
  <div class="partner-row">
    <span class="partner-badge"></span><span class="partner-badge"></span><span class="partner-badge"></span><span class="partner-badge"></span>
  </div>
</section>

<footer class="site-footer">
  <div class="footer-panel">
    <div class="footer-cols">
      <div><h4>Products</h4><ul><li>Cloud</li><li>IT Support</li><li>Voice Services</li><li>Connectivity</li></ul></div>
      <div><h4>Services</h4><ul><li>Business Owner</li><li>Office Managers</li><li>IT Managers</li><li>Enterprise</li></ul></div>
      <div><h4>Company</h4><ul><li>Contact Us</li><li>Blog</li><li>Careers</li><li>Legal Terms</li><li>Terms of Use</li><li>Privacy Policy</li></ul></div>
    </div>
    <div class="newsletter">
      <p>Subscribe To Our Newsletter</p>
      <div class="newsletter-field">E-mail<svg width="14" height="12" viewBox="0 0 14 12"><path d="M0 6h12M7 1l5 5-5 5" fill="none" stroke="#fff" stroke-width="1.6"/></svg></div>
    </div>
  </div>
  <div class="footer-brand"><span class="brand-mark"></span><span class="brand-name">Quil</span></div>
  <div class="footer-contact">
    <p>Street Address:</p>
    <p>Suite 4, 18 Carrow St,</p>
    <p>Ferndale NSW 2099</p>
    <p class="gap">Phone: +61 (2) 5550 1122</p>
    <p>Fax: +61 (2) 5550 1133</p>
    <p>Email: info@quilmo.net</p>
  </div>
  <div class="copyright">©2017 All Right Reserved</div>
</footer>

</body>
</html>
```